CBD Boutique Business Card Needed

We are in need of a business card to reflect the direction of our latest products. We are a fully organic company in which our store and products are very heavy in wood and "natural" components. We decided to bring color into one of our brands and immediately knew this is where we needed to go.

We are NOT a cash grab CBD company. We could have done this wrong, slapped a label on a shit product and left it like that. I am passionate about sharing my experience with other veterans and opening a store and making it a comfortable place for others to come and see if they can have the same experience.

Target Market(s)

We are a dual market company. We do have a beauty line that will cover the costs of the majority of our business. But we also heavily cater to veterans and first responders. I am a veteran and this is how I found out about CBD. So the marketing needs to bring in our higher end beauty clientele but also be able to not put off our customers that readily need this.

Contact Information for Business Card

What we are looking for is a light, professional, boutique design that is is neither quite feminine or masculine. Attached is a picture of a store in Portland that we asked our store designer to get her inspiration from. But all natural wood and black outlines are what is mostly in there.

Attached are the following files:

Logo: An AI file with how we have our logo. I do not understand AI and have no idea why the letters are individual. The font is Adam. OLU is the logo and Tonics of Vigor is our tagline.

KM Vantage (front and back) cards I did originally found at a trade show that I absolutely loved...while it is mostly there and I would still be happy with them but it is me pretending to be you. I understand I am not and there is probably a lot wrong that all of you would see instantly and this is why I am here.

Dropper Bottle: This is our final product mock up

Water Color: I am semi flexible here. This water color is slightly different on every level of our brand. The color itself can change...we are not stuck on THIS particular one. If you happen to make a new one that is similar in style and we use it...then I will happily commission you to change the rest on our next product run. I am pretty sure you can use this statement as evidence later . =) .

But seriously, we heavily believe in pay it forward and will work with anyone here that may have a vision bigger than ours. The winner of this contest will get preferential consideration on our marketing materials (need letterhead etc. next, as well as a brochure, and website) so three more projects coming down the pipeline.

Information to use for your mockup is contained on the card images I have included. I would prefer CBD for wellness CBD for life to be more prominent. No where else on the card do we have CBD mentioned.

Font styles to use
Sans Serif

Colors

Designer to choose colors to be used in the design.

Requirements
Must have
• Double Sided
• Front: OLU logo on front of card will be raised embossed. Background is watercolor. One has been provided. Others are up for consideration. If the rest of your design is incredible and I don't like your watercolor I will just ask to swap it.
• Back: Standard information. Not stuck on anything here. I LOVE clean minimal designs. The bleed on the card I provided is a luxury...
• Font for title and OLU is Adam. Everything else I prefer san serif or as clean as possible.
Nice to have
• I Need to incorporate Naturally Nurturing somewhere on the card. Bold but not intrusive.

```html
<!DOCTYPE html>
<html lang="en">
<head>
<meta charset="utf-8">
<title>OLU – Business Card</title>
<link rel="stylesheet" href="https://fonts.googleapis.com/css2?family=Montserrat:wght@400;500;700&display=swap">
<style>
  :root {
    --backdrop: #e9e6e2;
    --card: #ffffff;
    --ink: #3a3a3a;
    --teal: #16969a;
    --teal-soft: #7fcfd3;
    --teal-deep: #2aa3ad;
    --amber: #e0953a;
    --amber-soft: #f0b86a;
    --white: #ffffff;
  }
  * { box-sizing: border-box; margin: 0; padding: 0; }
  html, body { width: 1200px; height: 716px; overflow: hidden; }
  body {
    background: var(--backdrop);
    font-family: "Montserrat", sans-serif;
    color: var(--ink);
    position: relative;
  }
  .card {
    position: absolute;
    top: 198px;
    width: 560px;
    height: 320px;
    background: var(--card);
    overflow: hidden;
    box-shadow: 0 6px 18px rgba(0,0,0,.12);
  }
  .card--front { left: 27px; }
  .card--back { left: 613px; }

  /* Watercolour areas */
  .wash {
    position: absolute;
    border-radius: 46% 54% 48% 52% / 52% 44% 56% 48%;
    filter: blur(6px);
  }
  .card--front .wash {
    left: 80px; top: 18px; width: 400px; height: 280px;
    background: linear-gradient(170deg, var(--amber) 0%, var(--amber-soft) 38%, var(--teal-soft) 58%, var(--teal-deep) 80%, var(--teal-soft) 100%);
  }
  .card--back .wash {
    left: -30px; top: -40px; width: 380px; height: 240px;
    background: linear-gradient(165deg, var(--amber) 0%, var(--amber-soft) 30%, var(--teal-soft) 55%, var(--teal-deep) 78%, var(--teal-soft) 100%);
  }

  /* Front brand name */
  .brand {
    position: absolute;
    left: 0; right: 0; top: 112px;
    color: var(--white);
    text-align: center;
  }
  .brand__name {
    display: inline-flex;
    align-items: center;
    gap: 14px;
    font-size: 60px;
    font-weight: 500;
    line-height: 1;
    letter-spacing: 2px;
  }
  .brand__dot {
    width: 16px; height: 16px;
    border-radius: 50%;
    background: var(--white);
  }
  .brand__tagline {
    font-size: 18px;
    font-weight: 500;
    letter-spacing: .5px;
    margin-top: 14px;
  }

  /* Back */
  .person {
    position: absolute;
    left: 36px; top: 36px;
  }
  .person__name {
    color: var(--white);
    font-weight: 700;
    font-size: 30px;
    letter-spacing: .5px;
  }
  .person__title {
    font-size: 12px;
    font-weight: 500;
    letter-spacing: 1px;
    margin-top: 2px;
  }
  .slogan {
    position: absolute;
    right: 30px; top: 170px;
    color: var(--teal);
    font-size: 19px;
    font-weight: 400;
    letter-spacing: .3px;
  }
  .slogan span + span { margin-left: 14px; }
  .contact {
    position: absolute;
    right: 30px; top: 206px;
    list-style: none;
    text-align: right;
    font-size: 14px;
    line-height: 22px;
    letter-spacing: .6px;
  }
  .contact li { display: flex; justify-content: flex-end; align-items: center; gap: 10px; }
  .contact svg { width: 13px; height: 13px; fill: var(--teal); }
  .address {
    position: absolute;
    left: 36px; right: 30px; bottom: 22px;
    font-size: 14px;
    letter-spacing: .8px;
    text-align: right;
  }
</style>
</head>
<body>

<section class="card card--front">
  <div class="wash" role="img" aria-label="Orange and teal watercolour wash"></div>
  <div class="brand">
    <div class="brand__name"><span class="brand__dot"></span>OLU</div>
    <div class="brand__tagline">Tonics of Vigor</div>
  </div>
</section>

<section class="card card--back">
  <div class="wash" role="img" aria-label="Orange and teal watercolour wash"></div>
  <div class="person">
    <div class="person__name">Dana Whitfield</div>
    <div class="person__title">OWNER / CEO</div>
  </div>

  <p class="slogan"><span>CBD for wellness</span><span>CBD for life</span></p>

  <ul class="contact">
    <li>555.014.2280
      <svg viewBox="0 0 16 16" aria-hidden="true"><path d="M4 1h3l1 4-2 1.5a9 9 0 0 0 3.5 3.5L11 8l4 1v3c0 1-1 2-2 2C7 14 2 9 2 3c0-1 1-2 2-2z"/></svg>
    </li>
    <li>hello@olu.life
      <svg viewBox="0 0 16 16" aria-hidden="true"><path d="M1 3h14v10H1z M1 3l7 6 7-6" fill="none" stroke="#16969a" stroke-width="1.6"/></svg>
    </li>
    <li>www.olu.life
      <svg viewBox="0 0 16 16" aria-hidden="true"><g fill="none" stroke="#16969a" stroke-width="1.4"><circle cx="8" cy="8" r="6.5"/><ellipse cx="8" cy="8" rx="3" ry="6.5"/><path d="M1.5 8h13M3 4.5h10M3 11.5h10"/></g></svg>
    </li>
  </ul>

  <p class="address">1420 N Cedar Ave, Fairview, AZ 85000, Suite 210</p>
</section>

</body>
</html>
```